Velvor Display PowerPoint Design Project

We need PowerPoint slide templates for our Sales Media Kit at our re-branded company based in Canada called "Velvor Display Collective".

Looking for a look that clearly and powerfully portrays our unique and effective indoor advertising billboards in our network.

Our TinyPanes, WideSlats and GrandSheets are strategically placed in high traffic areas of restaurants, pubs, nightclubs, fitness clubs, colleges and universities, and sports arenas.

Key features of our media is a captive audience and 100% gender specific.

You can visit our old website for info on the above three media products (plorvex.ca)

Our Media Kits go out to small, medium business owners and advertising agenices.

Deliverables are:

1) Presentation cover slide with rich graphic content and space for content.
2) Presentation body slide with room for content 2 photos or logos. This slide should have the following:
a) No graphic in the text area
b) Space for page number at the bottom.
3) Photoshop (PSD) files for all graphic elements.
4) Font files for all fonts used.

Project Deadline Extended
Reason: Need more designs submitted.

We have uploaded our business card file.

Would like to incorporate the look, feel and colour of our business card to the power point template.

Target Market(s)

small business owners, marketing managers, media buyers and advertising agencies.

Industry/Entity Type

Advertising

Requirements
Must have
• We would like to see designs that:
- use the color scheme indicated by the attached logo design, perhaps expanding on it slightly.
- Look should be professional, smooth, and colourful.
-Must have a clean and modern feel that Ad Agencies would be impressed with.
-We have uploaded our business card file.

-Would like to incorporate the look, feel and colour of our business card to the power point template.

```html
<!DOCTYPE html>
<html lang="en">
<head>
<meta charset="utf-8">
<title>Velvor Display Collective – Presentation Templates</title>
<link rel="stylesheet" href="https://fonts.googleapis.com/css2?family=Source+Sans+3:wght@400;600;700&display=swap">
<style>
  :root {
    --stage: #a8a6a8;
    --brand-blue: #2e67b1;
    --deep-blue: #1f5fae;
    --chart-blue: #1f6fc4;
    --soft-blue: #a9bfe0;
    --band-grey: #8d9196;
    --title-grey: #7a7c80;
    --light-grey: #b5b5b5;
    --dark-grey: #5f5f5f;
    --ink: #1a1a1a;
    --paper: #ffffff;
  }
  * { box-sizing: border-box; margin: 0; padding: 0; }
  html, body { width: 1200px; height: 899px; overflow: hidden; }
  body {
    background: var(--stage);
    font-family: "Source Sans 3", sans-serif;
    position: relative;
  }
  .slide {
    position: absolute;
    width: 485px;
    height: 364px;
    background: var(--paper);
    box-shadow: 5px 6px 6px rgba(0,0,0,0.45);
    overflow: hidden;
  }
  .slide--cover   { left: 119px; top: 52px; }
  .slide--text    { left: 649px; top: 52px; }
  .slide--graphic { left: 119px; top: 463px; }
  .slide--charts  { left: 649px; top: 463px; }

  .slide__frame {
    position: absolute; left: 0; top: 0;
    width: 400px; height: 300px;
    transform: scale(1.2125);
    transform-origin: 0 0;
  }
  .slide__art { position: absolute; left: 0; top: 0; width: 400px; height: 300px; }

  .cover__brand {
    position: absolute; left: 0; width: 400px; top: 118px;
    text-align: center;
    font-size: 58px; font-weight: 700; color: var(--brand-blue);
    letter-spacing: -1px; line-height: 1;
  }
  .cover__title {
    position: absolute; left: 0; width: 400px; top: 179px;
    text-align: center;
    font-size: 15px; font-weight: 700; color: var(--title-grey);
    line-height: 22px;
  }
  .cover__subtitles {
    position: absolute; left: 57px; top: 233px;
    font-size: 10.5px; color: var(--deep-blue); line-height: 13px;
    list-style: none;
  }

  .slide__title {
    position: absolute; left: 0; width: 400px; top: 25px;
    text-align: center;
    font-size: 19px; font-weight: 700; color: var(--deep-blue);
  }
  .footer-brand {
    position: absolute; left: 5px; top: 268px;
    font-size: 21px; font-weight: 700; color: var(--brand-blue);
    letter-spacing: -0.5px;
  }
  .page-number {
    position: absolute; left: 380px; top: 287px;
    font-size: 6px; color: var(--paper);
  }

  .content-list { position: absolute; left: 15px; top: 70px; width: 355px; list-style: none; }
  .content-list__heading {
    font-size: 12.5px; font-weight: 700; color: var(--deep-blue);
    padding-left: 12px; position: relative;
  }
  .content-list__heading::before { content: "•"; position: absolute; left: 0; }
  .content-list__body {
    margin: 1px 0 0 27px; padding-left: 12px; position: relative;
    font-size: 11px; line-height: 12.6px; color: var(--ink);
  }
  .content-list__body::before { content: "–"; position: absolute; left: 0; }
  .content-list__items { list-style: none; margin: 3px 0 0 50px; }
  .content-list__items li {
    font-size: 9px; line-height: 13.4px; color: var(--ink);
    padding-left: 10px; position: relative;
  }
  .content-list__items li::before { content: "•"; position: absolute; left: 0; }

  .block-heading {
    position: absolute; top: 78px;
    font-size: 10.5px; font-weight: 700; color: var(--deep-blue);
  }
  .graphic-placeholder {
    position: absolute; left: 18px; top: 98px; width: 182px; height: 168px;
    background: radial-gradient(circle at 55% 55%, var(--chart-blue) 0 38%, var(--soft-blue) 39% 52%, var(--paper) 70%);
  }
  .chart-text { font-family: "Source Sans 3", sans-serif; font-size: 7px; fill: var(--ink); }
  .legend-text { font-family: "Source Sans 3", sans-serif; font-size: 8px; fill: var(--ink); }
</style>
</head>
<body>

<section class="slide slide--cover" aria-label="Cover slide">
  <div class="slide__frame">
    <svg class="slide__art" viewBox="0 0 400 300" aria-hidden="true">
      <path d="M0,0 H128 C70,40 58,120 74,175 C88,220 50,262 0,290 Z" fill="var(--band-grey)"/>
      <path d="M0,0 H112 C58,40 44,118 60,168 C74,212 40,248 0,272 Z" fill="var(--brand-blue)"/>
      <path d="M400,8 V300 H275 C312,250 330,205 338,150 C346,90 368,38 400,8 Z" fill="var(--band-grey)"/>
      <path d="M400,32 V300 H292 C328,252 345,205 352,155 C360,100 378,58 400,32 Z" fill="var(--brand-blue)"/>
    </svg>
    <div class="cover__brand">Velvor</div>
    <h1 class="cover__title">COMPANY PRESENTATION<br>TITLE HERE</h1>
    <ul class="cover__subtitles">
      <li>Subtitle Here</li>
      <li>Additional Texts</li>
      <li>Additional Texts</li>
    </ul>
  </div>
</section>

<section class="slide slide--text" aria-label="Text slide">
  <div class="slide__frame">
    <svg class="slide__art" viewBox="0 0 400 300" aria-hidden="true">
      <path d="M0,0 H135 C90,3 40,8 0,18 Z" fill="var(--band-grey)"/>
      <path d="M0,0 H125 C85,2 40,5 0,12 Z" fill="var(--brand-blue)"/>
      <path d="M70,300 C160,292 250,278 320,276 C360,275 385,280 400,288 V300 Z" fill="var(--band-grey)"/>
      <path d="M95,300 C180,295 260,284 325,282 C362,281 385,285 400,292 V300 Z" fill="var(--brand-blue)"/>
    </svg>
    <h2 class="slide__title">SLIDE TITLE HERE</h2>
    <ul class="content-list">
      <li class="content-list__heading">Slide Contents</li>
      <li class="content-list__body">The quick brown fox jumps over the lazy dog. The quick brown fox jumps over the lazy dog. The quick brown fox jumps over the lazy dog. The quick brown fox jumps over the lazy dog. The quick brown fox jumps over the lazy dog. The quick brown fox jumps over the lazy dog. The quick brown fox jumps over the lazy dog. The quick brown fox jumps over the lazy dog.</li>
    </ul>
    <ul class="content-list__items" style="position:absolute;left:15px;top:180px;">
      <li>Information</li><li>Content</li><li>Reports</li><li>Contacts</li><li>News</li><li>Information</li>
    </ul>
    <div class="footer-brand">Velvor</div>
    <div class="page-number">2</div>
  </div>
</section>

<section class="slide slide--graphic" aria-label="Graphic slide">
  <div class="slide__frame">
    <svg class="slide__art" viewBox="0 0 400 300" aria-hidden="true">
      <path d="M0,0 H135 C90,3 40,8 0,18 Z" fill="var(--band-grey)"/>
      <path d="M0,0 H125 C85,2 40,5 0,12 Z" fill="var(--brand-blue)"/>
      <path d="M70,300 C160,292 250,278 320,276 C360,275 385,280 400,288 V300 Z" fill="var(--band-grey)"/>
      <path d="M95,300 C180,295 260,284 325,282 C362,281 385,285 400,292 V300 Z" fill="var(--brand-blue)"/>
    </svg>
    <h2 class="slide__title">SLIDE TITLE HERE</h2>
    <h3 class="block-heading" style="left:24px;">Graphic Title</h3>
    <div class="graphic-placeholder" role="img" aria-label="Illustration of three blue gears turning with curved arrows"></div>
    <h3 class="block-heading" style="left:207px;">Title Here</h3>
    <svg class="slide__art" viewBox="0 0 400 300" role="img" aria-label="Stock chart with volume, open, high, low and close">
      <g class="chart-text" text-anchor="end">
        <text x="225" y="105">160</text><text x="225" y="119">140</text><text x="225" y="133">120</text>
        <text x="225" y="148">100</text><text x="225" y="162">80</text><text x="225" y="176">60</text>
        <text x="225" y="190">40</text><text x="225" y="205">20</text><text x="225" y="219">0</text>
      </g>
      <g class="chart-text">
        <text x="318" y="105">70</text><text x="318" y="119">60</text><text x="318" y="133">50</text>
        <text x="318" y="148">40</text><text x="318" y="162">30</text><text x="318" y="176">20</text>
        <text x="318" y="190">10</text><text x="318" y="219">0</text>
      </g>
      <line x1="230" y1="103" x2="230" y2="217" stroke="#999" stroke-width="0.5"/>
      <line x1="230" y1="217" x2="313" y2="217" stroke="#999" stroke-width="0.5"/>
      <line x1="313" y1="103" x2="313" y2="217" stroke="#999" stroke-width="0.5"/>
      <g fill="var(--chart-blue)">
        <rect x="238" y="146" width="5" height="71"/>
        <rect x="252" y="132" width="5" height="85"/>
        <rect x="266" y="110" width="5" height="107"/>
        <rect x="280" y="121" width="5" height="96"/>
        <rect x="294" y="112" width="5" height="105"/>
      </g>
      <g stroke="#333" stroke-width="0.5">
        <line x1="240" y1="130" x2="240" y2="170"/><line x1="254" y1="126" x2="254" y2="172"/>
        <line x1="268" y1="112" x2="268" y2="160"/><line x1="282" y1="118" x2="282" y2="162"/>
        <line x1="296" y1="120" x2="296" y2="160"/>
      </g>
      <rect x="237" y="138" width="6" height="22" fill="#444"/>
      <rect x="251" y="142" width="6" height="18" fill="#fff" stroke="#444" stroke-width="0.5"/>
      <rect x="265" y="126" width="6" height="18" fill="#fff" stroke="#444" stroke-width="0.5"/>
      <rect x="279" y="128" width="6" height="22" fill="#444"/>
      <rect x="293" y="134" width="6" height="14" fill="#fff" stroke="#444" stroke-width="0.5"/>
      <g class="chart-text">
        <text transform="translate(232,240) rotate(-45)">1/5/2002</text>
        <text transform="translate(260,240) rotate(-45)">1/7/2002</text>
        <text transform="translate(288,240) rotate(-45)">1/9/2002</text>
      </g>
      <rect x="335" y="147" width="5" height="5" fill="var(--chart-blue)"/>
      <g class="legend-text">
        <text x="343" y="153">Volume</text><text x="343" y="168">Open</text>
        <text x="343" y="183">High</text><text x="343" y="198">Low</text><text x="343" y="213">Close</text>
      </g>
    </svg>
    <div class="footer-brand">Velvor</div>
    <div class="page-number">3</div>
  </div>
</section>

<section class="slide slide--charts" aria-label="Chart slide">
  <div class="slide__frame">
    <svg class="slide__art" viewBox="0 0 400 300" aria-hidden="true">
      <path d="M0,0 H135 C90,3 40,8 0,18 Z" fill="var(--band-grey)"/>
      <path d="M0,0 H125 C85,2 40,5 0,12 Z" fill="var(--brand-blue)"/>
      <path d="M70,300 C160,292 250,278 320,276 C360,275 385,280 400,288 V300 Z" fill="var(--band-grey)"/>
      <path d="M95,300 C180,295 260,284 325,282 C362,281 385,285 400,292 V300 Z" fill="var(--brand-blue)"/>
    </svg>
    <h2 class="slide__title">SLIDE TITLE HERE</h2>
    <h3 class="block-heading" style="left:23px;">Click to Add Text Here</h3>
    <h3 class="block-heading" style="left:207px;">Click to Add Text Here</h3>
    <svg class="slide__art" viewBox="0 0 400 300" role="img" aria-label="Pie chart by quarter and area chart of two series">
      <path d="M60,183 L86,160 A35,35 0 1,1 28,153 Z" fill="var(--chart-blue)"/>
      <path d="M60,183 L28,153 A35,35 0 0,1 86,160 Z" fill="var(--light-grey)"/>
      <path d="M60,183 L86,160 A35,35 0 0,1 92,198 Z" fill="var(--dark-grey)"/>
      <line x1="86" y1="160" x2="115" y2="154" stroke="#888" stroke-width="0.5"/>
      <line x1="92" y1="198" x2="115" y2="210" stroke="#888" stroke-width="0.5"/>
      <rect x="115" y="154" width="30" height="28" fill="var(--light-grey)"/>
      <rect x="115" y="182" width="30" height="28" fill="#8f8f8f"/>
      <rect x="150" y="155" width="5" height="5" fill="var(--chart-blue)"/>
      <rect x="150" y="170" width="5" height="5" fill="var(--light-grey)"/>
      <rect x="150" y="185" width="5" height="5" fill="#8f8f8f"/>
      <rect x="150" y="200" width="5" height="5" fill="var(--dark-grey)"/>
      <g class="legend-text">
        <text x="159" y="161">1st Qtr</text><text x="159" y="176">2nd Qtr</text>
        <text x="159" y="191">3rd Qtr</text><text x="159" y="206">4th Qtr</text>
      </g>
      <g class="chart-text" text-anchor="end">
        <text x="222" y="139">40</text><text x="222" y="157">30</text><text x="222" y="174">20</text>
        <text x="222" y="192">10</text><text x="222" y="210">0</text>
      </g>
      <path d="M230,208 L236,130 L280,130 L276,208 Z" fill="none" stroke="#bbb" stroke-width="0.5"/>
      <path d="M240,145 L262,150 L275,182 L280,160 L280,195 L240,205 Z" fill="var(--light-grey)"/>
      <path d="M230,208 L230,150 L242,150 L252,160 L262,188 L270,180 L270,208 Z" fill="var(--chart-blue)"/>
      <text class="chart-text" x="282" y="214">Series 1</text>
      <text class="chart-text" x="208" y="226">1/5/2002</text>
      <rect x="335" y="172" width="5" height="5" fill="var(--chart-blue)"/>
      <rect x="335" y="187" width="5" height="5" fill="var(--light-grey)"/>
      <g class="legend-text">
        <text x="343" y="178">Series 1</text><text x="343" y="193">Series 2</text>
      </g>
    </svg>
    <div class="footer-brand">Velvor</div>
    <div class="page-number">4</div>
  </div>
</section>

</body>
</html>
```